Law Firm Website

We are looking to update our old, tired and very flat website. We have someone who will code and host the site but we need some design inspiration. The website will consist of no more than 2/3 pages, possibly with pop-ups for information. We already have all the blurb. We would like something distinctive, clean and eye-catching, using the purple and white theme that we already use on our firm stationery. Examples uploaded. Current website URL is www.dunmorewillett.example.

Industry/Entity Type

Law Firm

```html
<!DOCTYPE html>
<html lang="en">
<head>
<meta charset="utf-8">
<title>Dunmore + Willett Solicitors</title>
<link rel="stylesheet" href="https://fonts.googleapis.com/css2?family=Open+Sans:wght@400;600&family=Source+Sans+3:wght@400;600;700&display=swap">
<style>
:root{
  --purple:#5a4597;
  --purple-dark:#3b2d6e;
  --ink:#111111;
  --black:#000000;
  --white:#ffffff;
  --red:#b3262b;
  --photo-a:#8a8f96;
  --photo-b:#c9b59a;
  --photo-c:#4a4b52;
}
*{box-sizing:border-box;margin:0;padding:0}
html,body{width:1037px;height:1200px;overflow:hidden;background:var(--white)}
body{position:relative;font-family:"Source Sans 3",Arial,sans-serif;color:var(--ink)}
.abs{position:absolute}

/* header */
.brand-name{left:186px;top:26px;font-family:"Source Sans 3",sans-serif;font-weight:700;font-size:31px;letter-spacing:-.5px;color:var(--ink);line-height:1}
.brand-sub{left:239px;top:65px;font-weight:600;font-size:15px;color:var(--purple-dark)}
.contact-bar{right:186px;top:38px;display:flex;align-items:center;gap:8px;color:var(--purple)}
.contact-bar .phone{font-size:21px;font-weight:400;letter-spacing:.3px;margin-left:4px}
.social-dot{width:13px;height:13px;border-radius:50%;background:var(--ink)}
.main-nav{right:186px;top:69px;display:flex;gap:21px;font-size:13.5px}
.main-nav a{color:var(--purple);text-decoration:none}
.main-nav a.current{color:var(--ink)}

/* hero */
.hero-photo{left:0;top:118px;width:492px;height:348px;background:linear-gradient(110deg,var(--photo-c) 0%,var(--photo-a) 30%,#b8bcc4 55%,var(--photo-b) 80%,#d9c6a8 100%)}
.hero-panel{left:492px;top:118px;width:545px;height:348px;background:var(--purple)}
.hero-title{left:532px;top:186px;width:340px;font-family:"Open Sans",sans-serif;font-size:21.5px;line-height:23.5px;color:var(--white);letter-spacing:.3px}
.hero-points{left:532px;top:267px;list-style:none;color:var(--white);font-size:12.5px;line-height:19.5px}
.hero-points li{display:flex;align-items:center;gap:6px}
.cta{left:533px;top:338px}
.cta-label{left:558px;top:343px;font-weight:600;font-size:16px;color:var(--ink)}
.hero-more{left:533px;top:383px;font-size:9px;color:var(--white)}

/* news */
.news-band{left:0;top:466px;width:1037px;height:65px;background:var(--black);color:var(--white);text-align:center;font-size:9.5px}
.news-band .label{position:absolute;left:0;right:0;top:15px}
.news-band .item{position:absolute;left:0;right:0;top:35px}

/* welcome */
.welcome-title{left:0;right:0;top:571px;text-align:center;font-family:"Open Sans",sans-serif;font-size:19px;color:var(--purple-dark)}
.rule{height:1px;background:var(--ink)}
.rule::after{content:"";position:absolute;top:0;border-left:4px solid transparent;border-right:4px solid transparent;border-top:4px solid var(--ink)}
.welcome-rule{left:341px;top:610px;width:355px}
.welcome-rule::after{left:174px}
.welcome-text{left:196px;top:629px;width:645px;text-align:center;font-size:9.4px;line-height:15.6px}
.btn{background:var(--red);color:var(--white);font-family:"Open Sans",sans-serif;font-size:9px;letter-spacing:.6px;display:flex;align-items:center;justify-content:center}
.welcome-btn{left:479px;top:692px;width:79px;height:15px}

/* columns */
.section-title{display:flex;align-items:center;gap:8px;font-family:"Open Sans",sans-serif;font-size:16px;color:var(--ink)}
.testimonials-title{left:187px;top:748px}
.practice-title{left:493px;top:748px}
.testimonials-rule{left:186px;top:780px;width:266px}
.testimonials-rule::after{left:20px}
.practice-rule{left:492px;top:780px;width:355px}
.practice-rule::after{left:20px}
.quote{left:188px;width:270px;font-size:9px;line-height:10.5px}
.quote strong{display:block;font-family:"Open Sans",sans-serif;font-weight:600;font-size:9px}
.read-all{left:394px;top:948px;width:62px;height:15px}
.practice-photo{left:492px;top:794px;width:177px;height:168px;background:linear-gradient(90deg,#5a5d63 0%,#767a80 35%,#3a2e2a 60%,#6b5340 80%,#2e2622 100%)}
.practice-panel{left:669px;top:794px;width:181px;height:168px;background:var(--purple)}
.practice-list{left:685px;top:825px;list-style:none;color:var(--white);font-size:9.4px;line-height:13px}
.practice-list li::before{content:"›";margin-right:3px}
.practice-btn{left:684px;top:926px;width:82px;height:16px;box-shadow:1px 1px 2px rgba(0,0,0,.35)}

/* footer */
.site-footer{left:0;top:1050px;width:1037px;height:150px;background:var(--black);color:var(--white)}
.footer-nav{position:absolute;left:186px;top:55px;font-size:10.5px}
.footer-nav span{margin:0 4px}
.footer-contact{position:absolute;left:186px;top:79px;display:flex;align-items:center;gap:8px}
.footer-contact .phone{font-size:20px;margin-right:20px}
.footer-contact .social-dot{background:var(--white);width:15px;height:15px}
.copyright{position:absolute;right:189px;top:56px;font-size:11px}
</style>
</head>
<body>

<header>
  <div class="abs brand-name">Dunmore + Willett</div>
  <div class="abs brand-sub">Solicitors</div>
  <div class="abs contact-bar">
    <svg width="20" height="14" viewBox="0 0 20 14"><rect x="0.5" y="0.5" width="19" height="13" fill="var(--ink)"/><path d="M1 1 L10 8 L19 1" stroke="#fff" stroke-width="1.2" fill="none"/></svg>
    <span class="social-dot"></span>
    <span class="social-dot"></span>
    <svg width="11" height="16" viewBox="0 0 11 16"><rect x="1" y="1" width="9" height="14" rx="1.5" fill="none" stroke="var(--purple)" stroke-width="1.5"/><circle cx="5.5" cy="12.5" r="0.9" fill="var(--purple)"/></svg>
    <span class="phone">0300 555 0148</span>
  </div>
  <nav class="abs main-nav">
    <a href="#">Home</a>
    <a href="#" class="current">Area of Experties</a>
    <a href="#">Daniel Dunmore</a>
    <a href="#">Philip Willett</a>
    <a href="#">Contact Us</a>
  </nav>
</header>

<section>
  <div class="abs hero-photo" role="img" aria-label="Photo of a smiling solicitor in a suit meeting with a client across a desk"></div>
  <div class="abs hero-panel"></div>
  <h1 class="abs hero-title" style="font-weight:400">Lorem ipsum dolor sit amet, consectetur adipisicing elit, sed do eiusmod tempor incididunt</h1>
  <ul class="abs hero-points">
    <li><svg width="10" height="10" viewBox="0 0 10 10"><circle cx="5" cy="5" r="4.2" fill="none" stroke="#fff" stroke-width="1"/><path d="M3 5.2 L4.5 6.6 L7 3.6" stroke="#fff" stroke-width="1" fill="none"/></svg>Lore Ipsum sit amet donor adipising elit pretium elit</li>
    <li><svg width="10" height="10" viewBox="0 0 10 10"><circle cx="5" cy="5" r="4.2" fill="none" stroke="#fff" stroke-width="1"/><path d="M3 5.2 L4.5 6.6 L7 3.6" stroke="#fff" stroke-width="1" fill="none"/></svg>Donec sem eros, tincidunt at congue posuere donor</li>
    <li><svg width="10" height="10" viewBox="0 0 10 10"><circle cx="5" cy="5" r="4.2" fill="none" stroke="#fff" stroke-width="1"/><path d="M3 5.2 L4.5 6.6 L7 3.6" stroke="#fff" stroke-width="1" fill="none"/></svg>Sed eu non nil vehicula bibendum amet</li>
  </ul>
  <svg class="abs cta" width="161" height="33" viewBox="0 0 161 33"><path d="M0 0 H145 L161 16.5 L145 33 H0 Z" fill="var(--white)"/></svg>
  <div class="abs cta-label">Call to Action</div>
  <div class="abs hero-more">Learn More &gt;&gt;</div>
</section>

<section class="abs news-band">
  <div class="label">News and Blogs</div>
  <div class="item">June 09, 2014 : Lorem ipsum dolor sit amet, consectetur adipiscing elit. In fermentum dolor non augue pretium egestas. Learn More &gt;&gt;</div>
</section>

<section>
  <h2 class="abs welcome-title" style="font-weight:400">Welcome to Dunmore+Willett</h2>
  <div class="abs rule welcome-rule"></div>
  <p class="abs welcome-text">Lorem ipsum dolor sit amet, consectetur adipiscing elit. In fermentum dolor non augue pretium egestas. Donec sem eros, tincidunt at congue ut, posuere sit amet est. Vivamus scelerisque viverra odio sit amet laoreet. Ut nec neque non justo rutrum tempor lobortis eu ante.&nbsp; dolor Aliquam sagittis, nibh quis commodo auctor, risus nibh mauris laoreet lectus, id facilisis libero odio nec enim.</p>
  <div class="abs btn welcome-btn">Learn More</div>
</section>

<section>
  <div class="abs section-title testimonials-title">
    <svg width="19" height="14" viewBox="0 0 19 14"><circle cx="4" cy="9.5" r="4" fill="var(--ink)"/><path d="M1 9 Q1 2 7 0.5 L7.5 2 Q3.5 3.5 3.5 8 Z" fill="var(--ink)"/><circle cx="14" cy="9.5" r="4" fill="var(--ink)"/><path d="M11 9 Q11 2 17 0.5 L17.5 2 Q13.5 3.5 13.5 8 Z" fill="var(--ink)"/></svg>
    Testimonials
  </div>
  <div class="abs rule testimonials-rule"></div>
  <div class="abs quote" style="top:805px"><strong>David</strong>“Lorem ipsum dolor sit amet, consectetur amet adipiscing&nbsp; elit. In fermentum congu adipiscing sit amet, consectetur... ”</div>
  <div class="abs quote" style="top:853px"><strong>Peter</strong>“Lorem ipsum dolor sit amet, consectetur amet adipiscing&nbsp; elit. In fermentum congu adipiscing sit amet, consectetur... ”</div>
  <div class="abs quote" style="top:904px"><strong>Peter</strong>“Lorem ipsum dolor sit amet, consectetur amet adipiscing&nbsp; elit. In fermentum congu adipiscing sit amet, consectetur... ”</div>
  <div class="abs btn read-all">Read All</div>

  <div class="abs section-title practice-title">
    <svg width="21" height="19" viewBox="0 0 21 19"><path d="M10.5 0 L21 5 H0 Z" fill="var(--ink)"/><rect x="1" y="6" width="19" height="1.5" fill="var(--ink)"/><rect x="3" y="8.5" width="2.2" height="7" fill="var(--ink)"/><rect x="7.5" y="8.5" width="2.2" height="7" fill="var(--ink)"/><rect x="11.5" y="8.5" width="2.2" height="7" fill="var(--ink)"/><rect x="15.8" y="8.5" width="2.2" height="7" fill="var(--ink)"/><rect x="0" y="16.5" width="21" height="2.5" fill="var(--ink)"/></svg>
    Our Practice Areas
  </div>
  <div class="abs rule practice-rule"></div>
  <div class="abs practice-photo" role="img" aria-label="Photo of a lawyer in a grey suit with folded arms in front of law bookshelves"></div>
  <div class="abs practice-panel"></div>
  <ul class="abs practice-list">
    <li>Lorem ipsum dolor sit amet</li>
    <li>Consectetur Adipisicing</li>
    <li>Sed ut perspiciatis</li>
    <li>Procurements - Buying or Selling</li>
    <li>Sed ut perspiciatis unde omnis</li>
    <li>Accusamus et iusto</li>
    <li>Lorem ipsum dolor sit amet</li>
  </ul>
  <div class="abs btn practice-btn">Learn More</div>
</section>

<footer class="abs site-footer">
  <div class="footer-nav">Home<span>-</span>Area of Experties<span>-</span>Daniel Dunmore<span>-</span>Philip Willett<span>-</span>Contact</div>
  <div class="footer-contact">
    <svg width="12" height="17" viewBox="0 0 12 17"><rect x="1" y="1" width="10" height="15" rx="1.5" fill="none" stroke="#fff" stroke-width="1.6"/><circle cx="6" cy="13.3" r="1" fill="#fff"/></svg>
    <span class="phone">0300 555 0148</span>
    <span class="social-dot"></span>
    <span class="social-dot"></span>
    <svg width="20" height="15" viewBox="0 0 20 15"><rect x="0.5" y="0.5" width="19" height="14" fill="none" stroke="#fff" stroke-width="1.2"/><path d="M1 1 L10 8.5 L19 1 M1 14 L7.5 7 M19 14 L12.5 7" stroke="#fff" stroke-width="1.2" fill="none"/></svg>
  </div>
  <div class="copyright">© Copyright 2014</div>
</footer>

</body>
</html>
```